Kettle Pine Society - A Monthly Subscription Coffee Club - Shopify Website Design

A monthly subscription company. Need a Shopify Website Design and uploaded to fully work with Tidewell Renewals.

Please look at these sites for examples as well as the images I enclosed.

https://www.sipvaultory.com/
https://crumbcrate.com/
https://www.platewindly.com/
https://www.globalnibblers.com/

Number of Pages Required

1 page

```html
<!DOCTYPE html>
<html lang="en">
<head>
<meta charset="utf-8">
<title>Kettle Pine Society</title>
<link rel="stylesheet" href="https://fonts.googleapis.com/css2?family=Poppins:wght@400;500;600;700&display=swap">
<style>
:root{
  --ink:#5a4e45;
  --text:#3d3530;
  --muted:#6e635b;
  --accent:#9b3a50;
  --hero-bg:#f8f7f6;
  --band:#8a796d;
  --footer:#2d2724;
  --num:#c9c2bc;
  --white:#ffffff;
}
*{margin:0;padding:0;box-sizing:border-box}
html,body{width:1200px;height:2865px;overflow:hidden;background:var(--white)}
body{position:relative;font-family:"Poppins",sans-serif;color:var(--text)}
.abs{position:absolute}
.btn{position:absolute;background:var(--accent);color:var(--white);font-weight:600;font-size:12px;letter-spacing:.3px;display:flex;align-items:center;justify-content:center;border-radius:2px;text-transform:uppercase}

.hero{position:absolute;left:0;top:0;width:1200px;height:637px;background:var(--hero-bg)}
.nav-link{position:absolute;top:48px;font-size:12.5px;font-weight:500;color:var(--text)}
.brand{position:absolute;left:520px;top:44px;width:160px;display:flex;align-items:center;justify-content:center;gap:8px;font-size:14px;font-weight:600;color:var(--ink)}
.brand-dot{width:14px;height:14px;border-radius:50%;background:var(--ink)}
.login{left:922px;top:42px;width:75px;height:29px;font-size:11.5px;text-transform:none}
.cart{position:absolute;left:1020px;top:47px}
.hero-photo{position:absolute;left:540px;top:110px;width:660px;height:527px;background:radial-gradient(ellipse at 65% 45%,#6b4a34 0%,#9a8a80 35%,#ecebe9 70%,var(--hero-bg) 100%)}
.hero-title{position:absolute;left:155px;top:238px;font-size:80px;line-height:78px;font-weight:700;color:var(--ink);letter-spacing:1px}
.hero-copy{position:absolute;left:158px;top:397px;width:360px;font-size:12.5px;line-height:15px;color:var(--muted)}

.section-title{position:absolute;font-size:24px;font-weight:600;color:var(--ink)}
.why-item{position:absolute;top:770px;width:220px;text-align:center}
.why-item svg{display:block;margin:0 auto 12px}
.why-item h3{font-size:15.5px;font-weight:600;color:var(--ink)}
.why-item p{font-size:12.5px;color:var(--muted);margin-top:6px}

.bag-photo{position:absolute;left:0;top:946px;width:675px;height:449px;border-radius:0 225px 225px 0;background:linear-gradient(120deg,#6d5443 0%,#3d4258 45%,#c79b6e 80%,#e8dccf 100%)}
.bullets{position:absolute;left:727px;top:1073px;list-style:none}
.bullets li{display:flex;align-items:center;height:37px;font-size:12.5px;color:var(--muted)}
.bullets li::before{content:"";width:15px;height:15px;border-radius:50%;background:var(--ink);margin-right:14px}

.how-photo{position:absolute;left:525px;top:1433px;width:675px;height:449px;border-radius:225px 0 0 225px;background:linear-gradient(100deg,#d6d2ce 0%,#c9b7a4 45%,#b48d6e 70%,#615752 100%)}
.step{position:absolute;left:157px;display:flex;align-items:center}
.step-num{width:67px;font-size:38px;font-weight:600;color:var(--num)}
.step h3{font-size:15.5px;font-weight:600;color:var(--ink)}
.step p{font-size:12.5px;line-height:14px;color:var(--muted);width:210px}

.feed-sub{position:absolute;left:0;top:1984px;width:1200px;text-align:center;font-size:15.5px;color:var(--muted)}
.feed-sub b{color:var(--ink)}
.feed-tile{position:absolute;top:2044px;width:285px;height:285px}

.newsletter{position:absolute;left:0;top:2403px;width:1200px;height:178px;background:var(--band);color:var(--white);text-align:center}
.newsletter h2{margin-top:32px;font-size:24px;font-weight:600}
.newsletter p{font-size:15.5px;margin-top:4px}
.email{position:absolute;left:433px;top:103px;width:225px;height:37px;background:var(--white);border-radius:2px;font-size:12px;font-weight:500;color:#8a807a;text-align:left;padding-left:15px;line-height:37px}
.submit{left:662px;top:103px;width:150px;height:37px}

.footer{position:absolute;left:0;top:2581px;width:1200px;height:284px;background:var(--footer);color:var(--white)}
.footer-brand{position:absolute;left:157px;top:80px;font-size:19px;font-weight:600;line-height:26px;width:160px}
.footer-col{position:absolute;top:76px}
.footer-col h4{font-size:12px;font-weight:600;margin-bottom:9px}
.footer-col a{display:block;font-size:12.5px;line-height:22.5px;color:var(--white);text-decoration:none}
</style>
</head>
<body>

<header class="hero">
  <div class="hero-photo" role="img" aria-label="Steel scoop spilling roasted coffee beans"></div>
  <span class="nav-link" style="left:157px">Subscriptions</span>
  <span class="nav-link" style="left:296px">Coffees</span>
  <span class="nav-link" style="left:397px">FAQs</span>
  <div class="brand"><span class="brand-dot"></span>Kettle Pine Society</div>
  <div class="btn login">Login</div>
  <svg class="cart" width="24" height="22" viewBox="0 0 24 22" fill="none" stroke="#5a4e45" stroke-width="2"><path d="M1 2h4l3 12h12l3-9H7"/><circle cx="10" cy="19" r="1.6" fill="#5a4e45"/><circle cx="18" cy="19" r="1.6" fill="#5a4e45"/></svg>
  <h1 class="hero-title">Find your<br>Taste</h1>
  <p class="hero-copy">Lorem ipsum dolor sit amet, consectetur adipiscing elit, sed do eiusmod tempor incididunt ut labore et dolore</p>
  <div class="btn" style="left:158px;top:443px;width:150px;height:37px">Get Started</div>
</header>

<h2 class="section-title" style="left:0;top:705px;width:1200px;text-align:center">Why Kettle Pine Society?</h2>
<div class="why-item" style="left:108px">
  <svg width="44" height="40" viewBox="0 0 44 40" fill="none" stroke="#5a4e45" stroke-width="1.6"><path d="M10 16h22v8a9 9 0 0 1-9 9h-4a9 9 0 0 1-9-9z"/><path d="M32 18h3a3 3 0 0 1 0 6h-3"/><path d="M4 35h36"/><path d="M16 3c-2 3 2 5 0 9M21 3c-2 3 2 5 0 9M26 3c-2 3 2 5 0 9"/></svg>
  <h3>Perfect Taste</h3><p>Lorem Ipsum Ipsum</p>
</div>
<div class="why-item" style="left:365px">
  <svg width="44" height="40" viewBox="0 0 44 40" fill="none" stroke="#5a4e45" stroke-width="1.6"><circle cx="22" cy="20" r="15"/><path d="M15 20l5 5 9-10"/></svg>
  <h3>Fresh form Beans</h3><p>Lorem Ipsum Ipsum</p>
</div>
<div class="why-item" style="left:622px">
  <svg width="44" height="40" viewBox="0 0 44 40" fill="none" stroke="#5a4e45" stroke-width="1.6"><path d="M14 6h16v4l3 4v23H11V14l3-4z"/><path d="M14 10h16"/><rect x="17" y="20" width="10" height="10" rx="2"/></svg>
  <h3>New Flavor</h3><p>Lorem Ipsum Ipsum</p>
</div>
<div class="why-item" style="left:871px">
  <svg width="44" height="40" viewBox="0 0 44 40" fill="none" stroke="#5a4e45" stroke-width="1.4"><path d="M22 5l2 4 4 .5-3 3 .8 4-3.8-2-3.8 2 .8-4-3-3 4-.5z"/><path d="M11 11l1.5 3 3 .4-2.2 2 .5 3-2.8-1.5-2.8 1.5.5-3-2.2-2 3-.4z"/><path d="M33 11l1.5 3 3 .4-2.2 2 .5 3-2.8-1.5-2.8 1.5.5-3-2.2-2 3-.4z"/><path d="M16 36V26h4l3-5 2 1v4h5l-1 10z"/></svg>
  <h3>5-star Reviews</h3><p>Lorem Ipsum Ipsum</p>
</div>

<div class="bag-photo" role="img" aria-label="Barista scooping coffee beans into a paper bag"></div>
<h2 class="section-title" style="left:727px;top:1022px">What’s Inside The Bag?</h2>
<ul class="bullets">
  <li>Lorem ipsum dolor sit amet, consectetur</li>
  <li>Adipiscing elit, sed do eiusmod tempor</li>
  <li>Incididunt ut labore et dolore magna aliqua</li>
  <li>Lorem ipsum dolor sit amet, consectetur</li>
  <li>Adipiscing elit, sed do eiusmod tempor</li>
</ul>
<div class="btn" style="left:727px;top:1275px;width:150px;height:37px">Choose Plan</div>

<h2 class="section-title" style="left:157px;top:1490px">How It Works?</h2>
<div class="step" style="top:1548px"><span class="step-num">01</span><div><h3>Chose Plan</h3><p>Lorem ipsum dolor sit amet, consectetur adipiscing lacus vel</p></div></div>
<div class="step" style="top:1620px"><span class="step-num">02</span><div><h3>Ship Items</h3><p>Lorem ipsum dolor sit amet, consectetur adipiscing lacus vel</p></div></div>
<div class="step" style="top:1692px"><span class="step-num">03</span><div><h3>Enjoy Your Coffee</h3><p>Lorem ipsum dolor sit amet, consectetur adipiscing lacus vel</p></div></div>
<div class="btn" style="left:157px;top:1783px;width:150px;height:37px">Get Started</div>
<div class="how-photo" role="img" aria-label="Woman in a knit sweater sipping coffee by a window"></div>

<h2 class="section-title" style="left:0;top:1950px;width:1200px;text-align:center">Social Media Feed</h2>
<p class="feed-sub">Don’t forget to use our official hashtag <b>#KettlePineAlong</b></p>
<div class="feed-tile" style="left:157px;background:linear-gradient(135deg,#d9d3cd,#b9977a)" role="img" aria-label="Woman sipping coffee from a mug"></div>
<div class="feed-tile" style="left:457px;background:linear-gradient(135deg,#3a2e2a,#6b5648 60%,#d8c3ad)" role="img" aria-label="Friends holding latte art cups"></div>
<div class="feed-tile" style="left:756px;background:linear-gradient(135deg,#e6e1dc,#b8a08a 60%,#6f6a4a)" role="img" aria-label="Three friends sharing coffee at a café table"></div>

<section class="newsletter">
  <h2>Join Our Newsletter</h2>
  <p>Lorem ipsum dolor sit amet, consectetur adipiscing elit. In nec odio lorem.</p>
  <div class="email">You Email</div>
  <div class="btn submit">Submit</div>
</section>

<footer class="footer">
  <div class="footer-brand">Kettle Pine Society</div>
  <div class="footer-col" style="left:391px"><h4>SERVICES</h4><a>Subscriptions</a><a>Coffee Gifts</a></div>
  <div class="footer-col" style="left:648px"><h4>QUICK LINKS</h4><a>FAQs</a><a>Resources</a><a>Blogs</a></div>
  <div class="footer-col" style="left:907px"><h4>INFORMATION</h4><a>About Us</a><a>Contact Us</a><a>Terms &amp; Coniditions</a><a>Private Privacy</a></div>
</footer>

</body>
</html>
```